Discreet simple classy for adult entertainment

I would like a matte black business card with gold writing for my business. Keeping it simple. Having my following:

Lana frost
Events. Entertainment. Promotions
0491726580

or alternatively could have what i had on my previous card below but i think i prefer the above as again - discretion.

Maybe a nice gold line thru the card or some other very simple design . Or not open to ideas/ can be doublesided if any good ideas with that.

included pics of my old bus card. not sure weather i want a photo on it or not. if i do it wont be the same pic. i kinda wanted a card that was discreet so if it was in someones wallet they wouldn't neccessarily realise it was from a stripper.

Target Market(s)

men

Industry/Entity Type

Business

Contact Information for Business Card

Lana frost
0491726580

Requirements
Nice to have
• i don't know i am really open to anything. im giving my cards to guys so something they can have in their wallet that is discreet preferably.

```html
<!DOCTYPE html>
<html lang="en">
<head>
<meta charset="utf-8">
<title>Lana Frost – Business Card</title>
<link rel="stylesheet" href="https://fonts.googleapis.com/css2?family=Barlow+Condensed:wght@500;600&display=swap">
<style>
  :root {
    --page-bg: #e6e7e7;
    --card-black: #0b0b0b;
    --card-charcoal: #1c1c1c;
    --gold-light: #f3c640;
    --gold-mid: #d99a1c;
    --gold-deep: #9c5a14;
    --figure-light: #5a5a5a;
    --figure-dark: #1a1a1a;
  }
  html, body {
    margin: 0;
    width: 1200px;
    height: 1200px;
    overflow: hidden;
    background: var(--page-bg);
  }
  .canvas {
    position: relative;
    width: 1200px;
    height: 1200px;
  }
  .business-card {
    position: absolute;
    left: 80px;
    top: 275px;
    width: 1040px;
    height: 650px;
    border-radius: 56px;
    overflow: hidden;
    background:
      radial-gradient(ellipse at 70% 30%, var(--card-charcoal) 0%, var(--card-black) 70%);
  }
  .portrait-area {
    position: absolute;
    left: 124px;
    top: 77px;
    width: 340px;
    height: 573px;
    border-radius: 150px 150px 0 0;
    background: linear-gradient(180deg, var(--figure-light) 0%, #3a3a3a 45%, var(--figure-dark) 100%);
    opacity: 0.85;
  }
  .card-text {
    position: absolute;
    left: 518px;
    top: 228px;
    font-family: "Barlow Condensed", "Arial Narrow", sans-serif;
  }
  .gold-text {
    background: linear-gradient(90deg, var(--gold-light) 0%, var(--gold-mid) 55%, var(--gold-deep) 100%);
    -webkit-background-clip: text;
    background-clip: text;
    color: transparent;
    margin: 0;
    white-space: nowrap;
  }
  .owner-name {
    font-size: 88px;
    font-weight: 600;
    line-height: 1;
    letter-spacing: 1px;
    text-transform: uppercase;
  }
  .services {
    margin-top: 20px;
    font-size: 40px;
    font-weight: 500;
    line-height: 1;
  }
  .phone-number {
    margin-top: 16px;
    font-size: 60px;
    font-weight: 500;
    line-height: 1;
  }
</style>
</head>
<body>
  <main class="canvas">
    <section class="business-card">
      <div class="portrait-area" role="img" aria-label="Black and white photograph of a model in a gold Santa hat and gold accents"></div>
      <div class="card-text">
        <h1 class="gold-text owner-name">Lana Frost</h1>
        <p class="gold-text services">Events. Entertainment. Promotions</p>
        <p class="gold-text phone-number">0491726580</p>
      </div>
    </section>
  </main>
</body>
</html>
```